Brightfield Steel Depot (Metal Roofing Manufacturing and Supply) needs a billboard design

We need a billboard design for for our metal roofing manufacturing company in Sarasota FL, Brightfield Steel Depot Inc. You can visit our website www.brightfieldsteeldepot-example.com for more info about our company. We located are off Exit 210 on I 75- 482 Harrowgate Rd. Sarasota 34290
The billboard will be on I75 north of our office

I have a design that I am interested in but waiting on minor corrections from designer

```html
<!DOCTYPE html>
<html lang="en">
<head>
<meta charset="utf-8">
<title>Brightfield Steel Depot – Billboard</title>
<link rel="stylesheet" href="https://fonts.googleapis.com/css2?family=Archivo+Black&family=Noto+Sans:wght@400;700&family=Roboto:wght@400&display=swap">
<style>
  :root {
    --brand-blue: #1d4bb2;
    --brand-yellow: #ffe500;
    --sun-yellow: #f9d94a;
    --ink: #222222;
    --slate: #555555;
    --steel-light: #d8d8d8;
    --steel-dark: #8e8e8e;
    --paper: #ffffff;
    --backdrop: #eef1f5;
  }
  html, body {
    margin: 0;
    padding: 0;
    width: 958px;
    height: 1200px;
    overflow: hidden;
    background: var(--backdrop);
  }
  .billboard {
    position: absolute;
    left: 29px;
    top: 469px;
    width: 900px;
    height: 262px;
    box-shadow: 0 14px 24px rgba(0,0,0,0.22);
  }
  .billboard svg { display: block; }
  .brand-name {
    font-family: "Archivo Black", sans-serif;
    font-size: 23px;
    fill: var(--brand-blue);
  }
  .tab-label {
    font-family: "Archivo Black", sans-serif;
    font-size: 27px;
    fill: var(--ink);
  }
  .headline-main {
    font-family: "Archivo Black", sans-serif;
    font-size: 53px;
    fill: var(--brand-blue);
  }
  .headline-sub {
    font-family: "Archivo Black", sans-serif;
    font-size: 27.5px;
    fill: var(--brand-blue);
  }
  .headline-tail {
    font-family: "Roboto", sans-serif;
    font-size: 32px;
    fill: var(--slate);
    letter-spacing: 1px;
  }
  .quote-cta {
    font-family: "Noto Sans", sans-serif;
    font-size: 13.5px;
    fill: var(--brand-yellow);
  }
  .phone-number {
    font-family: "Archivo Black", sans-serif;
    font-size: 18px;
    fill: var(--paper);
  }
  .web-address {
    font-family: "Noto Sans", sans-serif;
    font-size: 12px;
    fill: var(--ink);
  }
  .web-address .domain { font-weight: 700; fill: var(--brand-blue); }
  .street-address {
    font-family: "Noto Sans", sans-serif;
    font-weight: 700;
    font-size: 13px;
    fill: var(--paper);
  }
</style>
</head>
<body>
<div class="billboard">
  <svg width="900" height="262" viewBox="0 0 900 262" xmlns="http://www.w3.org/2000/svg">
    <defs>
      <linearGradient id="roofPhotoTone" x1="0" y1="0" x2="1" y2="1">
        <stop offset="0" stop-color="#6a5650"/>
        <stop offset="0.45" stop-color="#8b7770"/>
        <stop offset="0.6" stop-color="#d9d4cf"/>
        <stop offset="1" stop-color="#5c4842"/>
      </linearGradient>
      <linearGradient id="steelTab" x1="0" y1="0" x2="1" y2="0">
        <stop offset="0" stop-color="var(--steel-dark)"/>
        <stop offset="0.5" stop-color="var(--steel-light)"/>
        <stop offset="1" stop-color="#bdbdbd"/>
      </linearGradient>
      <linearGradient id="steelRule" x1="0" y1="0" x2="1" y2="0">
        <stop offset="0" stop-color="#999"/>
        <stop offset="1" stop-color="#ddd"/>
      </linearGradient>
    </defs>

    <!-- base panel -->
    <rect class="panel" x="0" y="0" width="900" height="262" fill="var(--paper)"/>

    <!-- photo area -->
    <polygon class="roof-photo" role="img" aria-label="Photo of a house with brown standing-seam metal roof and dormer windows"
             points="608,0 900,0 900,262 526,262" fill="url(#roofPhotoTone)"/>

    <!-- accent shapes -->
    <polygon class="accent-yellow" points="0,0 54,0 0,101" fill="var(--brand-yellow)"/>
    <polygon class="accent-blue" points="557,0 608,0 583,73" fill="var(--brand-blue)"/>

    <!-- brand block -->
    <circle class="brand-mark" cx="120" cy="62" r="36" fill="var(--sun-yellow)"/>
    <text class="brand-name" x="120" y="138" text-anchor="middle">Brightfield</text>
    <text class="brand-name" x="120" y="166" text-anchor="middle">Steel Depot</text>

    <!-- headline -->
    <polygon class="metal-tab" points="203,29 345,29 360,62 219,62" fill="url(#steelTab)"/>
    <rect class="metal-rule" x="358" y="61" width="165" height="1.5" fill="url(#steelRule)"/>
    <text class="tab-label" x="225" y="56">METAL</text>
    <text class="headline-main" x="219" y="124">ROOFING</text>
    <text class="headline-sub" x="219" y="157">MANUFACTURING</text>
    <text class="headline-tail" x="531" y="191" text-anchor="end">AND SUPPLY</text>

    <!-- bottom band -->
    <polygon class="band-blue-base" points="0,252 620,252 626,262 0,262" fill="var(--brand-blue)"/>
    <polygon class="band-blue-left" points="0,209 230,209 268,262 0,262" fill="var(--brand-blue)"/>
    <polygon class="band-yellow-outline" points="236,211 580,211 612,262 276,262" fill="var(--paper)"/>
    <polygon class="band-yellow" points="244,214 575,214 600,251 270,251" fill="var(--brand-yellow)"/>
    <polygon class="band-blue-right" points="546,219 900,219 900,262 575,262" fill="var(--brand-blue)" fill-opacity="0.88"/>

    <!-- quote and phone -->
    <text class="quote-cta" x="37" y="228">Get your quote today!</text>
    <g class="icon-phone" transform="translate(45,247)">
      <circle r="8" fill="var(--paper)"/>
      <circle r="6.3" fill="var(--brand-yellow)"/>
      <path d="M-3.2,-3.6 l1.6,-0.6 l1.2,2.2 l-1,0.9 q0.8,1.8 2.6,2.6 l0.9,-1 l2.2,1.2 l-0.6,1.6 q-0.8,0.8 -2.2,0.4 q-4,-1.4 -5.2,-5.2 q-0.3,-1.4 0.5,-2.1z" fill="var(--brand-blue)"/>
    </g>
    <text class="phone-number" x="59" y="254">941-555-0142</text>

    <!-- web address -->
    <g class="icon-globe" transform="translate(297,237)" fill="none" stroke="var(--ink)" stroke-width="0.9">
      <circle r="6.5"/>
      <ellipse rx="3" ry="6.5"/>
      <line x1="-6.5" y1="0" x2="6.5" y2="0"/>
      <line x1="-5.6" y1="-3.3" x2="5.6" y2="-3.3"/>
      <line x1="-5.6" y1="3.3" x2="5.6" y2="3.3"/>
    </g>
    <text class="web-address" x="309" y="241">www.<tspan class="domain">brightfieldsteeldepot-example</tspan>.com</text>

    <!-- street address -->
    <g class="icon-pin" transform="translate(600,241)" fill="none" stroke="var(--brand-yellow)" stroke-width="1">
      <circle r="7.5"/>
      <path d="M0,4.5 C-3.5,0.5 -3.5,-1 -3.5,-1.5 A3.5,3.5 0 0 1 3.5,-1.5 C3.5,-1 3.5,0.5 0,4.5z" fill="var(--brand-yellow)" stroke="none"/>
      <circle cx="0" cy="-1.5" r="1.3" fill="var(--brand-blue)" stroke="none"/>
    </g>
    <text class="street-address" x="612" y="246">482 Harrowgate Road Sarasota, Fl 34290</text>
  </svg>
</div>
</body>
</html>
```